4 'Thank you' greetings cards designs

We are a small greetings card publisher and we need designs for a range of 'Thank you' greetings cards and notecards.
This project is for a total of 4 designs.
Please take a look at this board on Moodpinly, to see the kind of thing we are looking for: https://www.moodpinly.example/dorvek481/thank-you-cards/
The cards will be printed at a maximum size of 131mm x 183mm (including a 3mm bleed) so please provide 300dpi CMYK files at this size. Please ensure that any text (or elements of the design that are not part of the bleed) are at least 11mm in from each edge. Also, please note that cards do not have to have a bleed if your design doesn't require it (e.g. a plain white background).
Please provide 2 designs in 'portrait' orientation and 2 in 'landscape'.
Please provide 2 designs that just have the words 'Thank you' and then 2 designs that include your choice of these alternative messages:
Thank you so much
Thanks very much
Thank you very much
Thanks a million
Just to say thank you
A big thank you
A really big thank you
Feel free to use an exclamation mark on a couple of your designs, if you wish!
Other than the above guidelines, everything else is up to you in terms of colours, fonts, shapes, etc. - but please use the Moodpinly board to see the kind of designs we are looking for.
Thank you!

```html
<!DOCTYPE html>
<html lang="en">
<head>
<meta charset="utf-8">
<title>Thank You Cards – Floral Watercolour Pair</title>
<link rel="stylesheet" href="https://fonts.googleapis.com/css2?family=Kalam:wght@400;700&display=swap">
<style>
  :root {
    --backdrop: #f3f1f4;
    --card: #ffffff;
    --card-edge: #e6e2e8;
    --rose: #e8457e;
    --rose-soft: #f29ab9;
    --violet: #8a6cc4;
    --violet-soft: #b9a5de;
    --teal: #2fa7c6;
    --teal-soft: #8fd0df;
    --berry: #c2448a;
  }
  * { box-sizing: border-box; margin: 0; padding: 0; }
  html, body {
    width: 1200px;
    height: 1200px;
    overflow: hidden;
    background: var(--backdrop);
  }
  .card-set {
    position: relative;
    width: 1200px;
    height: 1200px;
    display: flex;
    justify-content: center;
    align-items: center;
    gap: 60px;
  }
  .card {
    position: relative;
    width: 480px;
    height: 640px;
    background: var(--card);
    border: 1px solid var(--card-edge);
  }
  .floral-frame {
    position: absolute;
    inset: 38px;
  }
  .floral-frame--rose {
    background:
      radial-gradient(circle at 18% 12%, var(--rose) 0 9%, transparent 22%),
      radial-gradient(circle at 62% 10%, var(--rose-soft) 0 8%, transparent 20%),
      radial-gradient(circle at 88% 8%, var(--violet) 0 6%, transparent 16%),
      radial-gradient(circle at 80% 88%, var(--rose) 0 10%, transparent 22%),
      radial-gradient(circle at 36% 86%, var(--rose) 0 8%, transparent 20%),
      radial-gradient(circle at 12% 94%, var(--violet) 0 6%, transparent 16%),
      linear-gradient(160deg, var(--teal-soft), var(--violet-soft) 50%, var(--teal-soft));
  }
  .floral-frame--teal {
    background:
      radial-gradient(circle at 20% 10%, var(--rose) 0 9%, transparent 22%),
      radial-gradient(circle at 70% 22%, var(--rose) 0 8%, transparent 20%),
      radial-gradient(circle at 90% 18%, var(--violet) 0 6%, transparent 16%),
      radial-gradient(circle at 64% 90%, var(--rose) 0 10%, transparent 22%),
      radial-gradient(circle at 22% 86%, var(--rose-soft) 0 8%, transparent 20%),
      linear-gradient(200deg, var(--violet-soft), var(--teal-soft) 50%, var(--violet-soft));
  }
  .message-panel {
    position: absolute;
    top: 30%;
    left: 22%;
    width: 56%;
    height: 38%;
    background: var(--card);
    border-radius: 46%;
    display: flex;
    flex-direction: column;
    justify-content: center;
    align-items: center;
  }
  .greeting {
    font-family: "Kalam", cursive;
    font-weight: 400;
    line-height: 0.95;
    text-align: center;
  }
  .greeting--mixed { font-size: 62px; }
  .greeting--mixed .word-thank { color: var(--teal); display: block; }
  .greeting--mixed .word-you { color: var(--berry); display: block; padding-left: 40px; }
  .greeting--teal { font-size: 72px; color: var(--teal); }
  .greeting--teal span { display: block; }
  .greeting--teal .word-you { padding-left: 50px; }
</style>
</head>
<body>
  <main class="card-set">
    <article class="card card--rose">
      <div class="floral-frame floral-frame--rose" role="img" aria-label="Watercolour border of pink and violet flowers with teal and purple leaves surrounding the message"></div>
      <div class="message-panel">
        <p class="greeting greeting--mixed"><span class="word-thank">Thank</span><span class="word-you">You</span></p>
      </div>
    </article>
    <article class="card card--teal">
      <div class="floral-frame floral-frame--teal" role="img" aria-label="Watercolour border of pink flowers, violet blooms and teal leaves arranged around the message"></div>
      <div class="message-panel">
        <p class="greeting greeting--teal"><span class="word-thank">Thank</span><span class="word-you">You</span></p>
      </div>
    </article>
  </main>
</body>
</html>
```